Dental Specialist Needs a Business Card

We are a state of the art dental specialty office and need a business card that looks modern but professional.
I have provided our logo design in both vertical and horizontal. We use the design on letterhead in the vertical format but provided both forms for you. Thanks

Please add the address, phone and fax numbers I listed to all designs and please leave a space for website and for my employee name on each design. Thanks 2847 Halloway Avenue, Suite K East Marlow, NY 14391 Phone (716)382-9157 Fax:(716)382-9150 My name is Miles R.Dunford,D.D.S. If you want to show it with my name but the design needs to allow for the name to be switched.

Industry/Entity Type

Business

```html
<!DOCTYPE html>
<html lang="en">
<head>
<meta charset="utf-8">
<title>Keystone Endodontics P.C. — Business Card</title>
<link rel="stylesheet" href="https://fonts.googleapis.com/css2?family=Domine:wght@400;500&display=swap">
<style>
  :root {
    --backdrop: #3a3838;
    --card: #ffffff;
    --ink: #1c1c1c;
    --sky: #1fb4ec;
    --rule: #9a9a9a;
  }
  * { margin: 0; padding: 0; box-sizing: border-box; }
  html, body {
    width: 1200px; height: 900px; overflow: hidden;
    background: var(--backdrop);
    font-family: "Domine", Georgia, serif;
    color: var(--ink);
  }
  .business-card {
    position: absolute; left: 100px; top: 164px;
    width: 1000px; height: 572px;
    background: var(--card);
    overflow: hidden;
  }
  .brand {
    position: absolute; left: 56px; top: 56px;
    display: flex; align-items: center;
  }
  .brand-mark {
    width: 84px; height: 84px; border-radius: 50%;
    background: var(--sky);
  }
  .brand-divider {
    width: 1px; height: 120px; background: var(--rule);
    margin: 0 26px 0 28px;
  }
  .brand-name { font-weight: 400; color: var(--ink); line-height: 1; }
  .brand-name .primary { display: block; font-size: 62px; letter-spacing: 1px; }
  .brand-name .secondary { display: block; font-size: 22px; letter-spacing: 3px; margin-top: 8px; }

  .holder {
    position: absolute; left: 40px; top: 376px;
    width: 284px;
  }
  .holder-name { font-size: 33px; font-weight: 500; line-height: 1.1; white-space: nowrap; }
  .holder-title { font-size: 19px; margin-top: 6px; white-space: nowrap; }

  .contact-divider {
    position: absolute; left: 342px; top: 360px;
    width: 1px; height: 124px; background: var(--sky);
  }
  .contact {
    position: absolute; left: 366px; top: 376px;
    list-style: none; font-size: 21px; line-height: 32px;
  }
  .contact li { display: flex; align-items: center; white-space: nowrap; }
  .contact .icon { width: 20px; height: 20px; margin-right: 14px; flex: none; }
  .contact .inline-icon { width: 18px; height: 18px; margin: 0 8px 0 22px; }

  .footer-band {
    position: absolute; left: 0; bottom: 0;
    width: 100%; height: 30px; background: var(--sky);
  }
</style>
</head>
<body>
  <article class="business-card">
    <header class="brand">
      <span class="brand-mark" aria-hidden="true"></span>
      <span class="brand-divider" aria-hidden="true"></span>
      <h1 class="brand-name">
        <span class="primary">KEYSTONE</span>
        <span class="secondary">Endodontics P.C.</span>
      </h1>
    </header>

    <section class="holder">
      <p class="holder-name">Miles R. Dunford</p>
      <p class="holder-title">Doctor of Dental Surgery</p>
    </section>

    <span class="contact-divider" aria-hidden="true"></span>

    <ul class="contact">
      <li>
        <svg class="icon" viewBox="0 0 20 20" aria-hidden="true"><path d="M10 1a6 6 0 0 0-6 6c0 4.5 6 12 6 12s6-7.5 6-12a6 6 0 0 0-6-6z" fill="#1fb4ec"/><circle cx="10" cy="7" r="2.3" fill="#fff"/></svg>
        2847 Halloway Avenue, Suite K, East Marlow, NY 14391
      </li>
      <li>
        <svg class="icon" viewBox="0 0 20 20" aria-hidden="true"><path d="M5 2l3 4-2 2c1 2.5 3.5 5 6 6l2-2 4 3-2 3C9 18 2 11 2 4z" fill="#1fb4ec"/></svg>
        (716) 382-9157
        <svg class="icon inline-icon" viewBox="0 0 20 20" aria-hidden="true"><rect x="5" y="2" width="10" height="6" fill="#1fb4ec"/><rect x="2" y="8" width="16" height="7" rx="1" fill="#1fb4ec"/><rect x="5" y="13" width="10" height="5" fill="#fff" stroke="#1fb4ec" stroke-width="1.5"/></svg>
        (716) 382-9150
      </li>
      <li>
        <svg class="icon" viewBox="0 0 20 20" aria-hidden="true"><circle cx="10" cy="10" r="8" fill="none" stroke="#1fb4ec" stroke-width="2"/><ellipse cx="10" cy="10" rx="3.5" ry="8" fill="none" stroke="#1fb4ec" stroke-width="1.5"/><path d="M2 10h16" stroke="#1fb4ec" stroke-width="1.5"/></svg>
        www.keystoneendo.com
      </li>
    </ul>

    <span class="footer-band" aria-hidden="true"></span>
  </article>
</body>
</html>
```